Webdesign for silver path

"Der Sternenpfad" is a new info product that will be selled through the website maybe you will create for us.

Translated from german to english the project is named "the silver path". It´s an online video course that teaches people how to live a fulfilling, happy and healthy life.

Design paramaters
We want a serious design that embodies the real feeling of beeing happy and fulfilled. Visitors should even feel good/better when they see the website.
In color psychology some sort of calming deep green like a four-leaf clover is recommend.
Mainly the website will be the external sales page with a big video as the central attention.
We also need a member area for customers to watch our video course.

So mainly we need a eye-cathing, calming header, the content body with mainly video and just a few written words...and of course a footer for links like imprint, affiliate program etc.

What we not want:
- some kind of these exaggerated smiling photos
- that bathetic luck symbols like money or boats
Updates

Hi,

i posted a message to the design discussion. Thank you!

Industry/Entity Type

Affiliate

```html
<!DOCTYPE html>
<html lang="de">
<head>
<meta charset="utf-8">
<title>Der Sternenpfad</title>
<link rel="stylesheet" href="https://fonts.googleapis.com/css2?family=Raleway:wght@300;400;500&family=Open+Sans:wght@600;700&display=swap">
<style>
  :root {
    --green-deep: #1e3510;
    --green-dark: #34521a;
    --green-mid: #5f8420;
    --green-bright: #a6cc2c;
    --button-top: #8fb42a;
    --button-bottom: #6a8e19;
    --text-light: #e9eddc;
    --text-soft: #cfd8bd;
    --footer-bg: #ffffff;
    --footer-text: #4a4a4a;
    --player-bar: #e6e6e6;
    --icon-blue: #3b7fc4;
  }
  * { box-sizing: border-box; margin: 0; padding: 0; }
  html, body { width: 1200px; height: 1052px; overflow: hidden; }
  body {
    position: relative;
    font-family: "Raleway", sans-serif;
    background: var(--footer-bg);
  }
  .site-header {
    position: absolute; left: 0; top: 0; width: 1200px; height: 146px;
    background: radial-gradient(ellipse 420px 160px at 560px 20px, #7f9d28 0%, transparent 100%),
                linear-gradient(180deg, #627f1c 0%, #4b6a14 70%, #3b5510 100%);
  }
  .brand {
    position: absolute; left: 136px; top: 32px; display: flex; align-items: center; gap: 30px;
  }
  .brand-mark {
    width: 90px; height: 90px; border-radius: 50%; background: #f0b419;
  }
  .brand-name {
    font-family: "Raleway", sans-serif; font-weight: 300; font-size: 40px;
    color: #dfe5c8; letter-spacing: 0.5px; text-transform: uppercase;
  }
  .header-nav { position: absolute; top: 53px; left: 883px; display: flex; gap: 18px; }
  .nav-button {
    width: 87px; height: 36px; border-radius: 4px;
    background: linear-gradient(180deg, var(--button-top), var(--button-bottom));
    box-shadow: 0 2px 3px rgba(0,0,0,.35), inset 0 1px 0 rgba(255,255,255,.35);
    color: #fff; font-family: "Open Sans", sans-serif; font-weight: 700; font-size: 15px;
    display: flex; align-items: center; justify-content: center;
    text-shadow: 0 1px 1px rgba(0,0,0,.35);
  }
  .stage {
    position: absolute; left: 0; top: 146px; width: 1200px; height: 762px;
    background: radial-gradient(ellipse 520px 420px at 600px 0px, var(--green-bright) 0%, var(--green-mid) 45%, transparent 100%),
                radial-gradient(ellipse 900px 700px at 600px 200px, #577a1c 0%, var(--green-dark) 60%, var(--green-deep) 100%);
  }
  .player {
    position: absolute; left: 130px; top: 58px; width: 548px; height: 412px;
    box-shadow: 0 24px 22px -14px rgba(0,0,0,.55);
  }
  .player-screen {
    width: 548px; height: 379px;
    background: radial-gradient(ellipse 250px 200px at 50% 42%, #3d3d3d 0%, #141414 65%, #000 100%);
    position: relative; border-top: 5px solid #000;
  }
  .player-title {
    position: absolute; top: 142px; width: 100%; text-align: center;
    font-family: "Raleway", sans-serif; font-weight: 300; font-size: 50px; color: #9c9c9c;
    text-transform: uppercase;
  }
  .play-badge {
    position: absolute; background: rgba(255,255,255,.3); border-radius: 4px;
    display: flex; align-items: center; justify-content: center;
  }
  .player-screen .play-badge { left: 242px; top: 149px; width: 68px; height: 68px; }
  .player-bar {
    height: 33px; background: linear-gradient(180deg, #fafafa, var(--player-bar));
    display: flex; align-items: center; font-family: "Open Sans", sans-serif; font-size: 11px; color: #222;
    border-top: 1px solid #bbb;
  }
  .bar-cell { height: 100%; display: flex; align-items: center; padding: 0 7px; border-right: 1px solid #c4c4c4; }
  .bar-track { flex: 1; border-right: none; }
  .bar-track span { display: block; width: 100%; height: 6px; background: #b9b9b9; border-radius: 3px; }
  .video-list {
    position: absolute; left: 733px; top: 60px; width: 334px; height: 353px;
    background: rgba(210,225,170,.22); border-radius: 3px; padding: 20px 0 0 24px;
  }
  .video-item { display: flex; align-items: center; height: 106px; }
  .video-thumb { position: relative; width: 146px; height: 94px; flex: none; }
  .video-thumb .play-badge { left: 46px; top: 18px; width: 58px; height: 58px; }
  .thumb-sunset { background: linear-gradient(180deg, #e0621c 0%, #f4a21e 55%, #2a1a08 85%); }
  .thumb-sky { background: linear-gradient(135deg, #2a4d7c 0%, #8fa8c8 45%, #dfe6ee 100%); }
  .thumb-dusk { background: linear-gradient(180deg, #7b3b8a 0%, #c55a88 55%, #2d1a2a 90%); }
  .video-caption {
    margin-left: 22px; color: var(--text-light); font-size: 16px; line-height: 20.5px; font-weight: 500;
  }
  .buy-button {
    position: absolute; left: 733px; top: 428px; width: 334px; height: 46px; border-radius: 4px;
    background: linear-gradient(180deg, var(--button-top), var(--button-bottom));
    box-shadow: 0 14px 16px -8px rgba(0,0,0,.5), inset 0 1px 0 rgba(255,255,255,.35);
    color: #fff; font-family: "Open Sans", sans-serif; font-weight: 600; font-size: 22px;
    display: flex; align-items: center; justify-content: center; text-shadow: 0 1px 1px rgba(0,0,0,.3);
  }
  .divider {
    position: absolute; left: 100px; top: 561px; width: 1000px; height: 1px;
    background: linear-gradient(90deg, transparent, rgba(255,255,255,.65) 8%, rgba(255,255,255,.65) 92%, transparent);
  }
  .intro {
    position: absolute; left: 140px; top: 592px; width: 918px;
    color: var(--text-soft); font-size: 16px; line-height: 22.7px; font-weight: 400;
    text-align: justify; text-align-last: center;
  }
  .site-footer {
    position: absolute; left: 0; top: 908px; width: 1200px; height: 144px; background: var(--footer-bg);
  }
  .copyright {
    position: absolute; left: 126px; top: 35px; color: var(--footer-text); font-size: 14px; font-weight: 500;
  }
  .social { position: absolute; left: 845px; top: 22px; display: flex; }
  .social-link {
    width: 62px; height: 46px; display: flex; align-items: center; justify-content: center;
    border-left: 1px solid #e2e2e2;
  }
  .social-link:first-child { border-left: none; }
  .social-link span { width: 32px; height: 32px; border-radius: 4px; background: var(--icon-blue); }
  .social-link:nth-child(1) span { background: #5bc2e8; }
  .social-link:nth-child(3) span { background: #d6d6d6; }
</style>
</head>
<body>
  <header class="site-header">
    <div class="brand">
      <span class="brand-mark"></span>
      <span class="brand-name">Der Sternenpfad</span>
    </div>
    <nav class="header-nav">
      <span class="nav-button">Affliate</span>
      <span class="nav-button">Login</span>
    </nav>
  </header>

  <main class="stage">
    <section class="player">
      <div class="player-screen">
        <div class="player-title">Der Sternenpfad</div>
        <div class="play-badge">
          <svg width="28" height="32" viewBox="0 0 28 32"><path d="M2 2 L26 16 L2 30 Z" fill="#fff"/></svg>
        </div>
      </div>
      <div class="player-bar">
        <div class="bar-cell"><svg width="8" height="10" viewBox="0 0 8 10"><path d="M0 0 L8 5 L0 10 Z" fill="#111"/></svg></div>
        <div class="bar-cell">00:00</div>
        <div class="bar-cell bar-track"><span></span></div>
        <div class="bar-cell">00:00</div>
        <div class="bar-cell"><svg width="32" height="14" viewBox="0 0 32 14"><path d="M0 4 H3 L7 1 V13 L3 10 H0 Z" fill="#222"/><path d="M10 9v2M13 8v4M16 7v6M19 6v8M22 4v10M25 3v11M28 2v12" stroke="#333" stroke-width="1.5"/></svg></div>
        <div class="bar-cell" style="border-right:none"><svg width="12" height="12" viewBox="0 0 12 12"><path d="M1 4V1h3M8 1h3v3M11 8v3H8M4 11H1V8" stroke="#222" stroke-width="1.5" fill="none"/></svg></div>
      </div>
    </section>

    <aside class="video-list">
      <div class="video-item">
        <div class="video-thumb thumb-sunset" role="img" aria-label="Silhouetted family cheering against an orange sunset">
          <div class="play-badge"><svg width="22" height="26" viewBox="0 0 22 26"><path d="M1 1 L21 13 L1 25 Z" fill="#fff"/></svg></div>
        </div>
        <p class="video-caption">Member Video<br>Lorem ipsum<br>sit amet.....</p>
      </div>
      <div class="video-item">
        <div class="video-thumb thumb-sky" role="img" aria-label="Child holding a globe under a cloudy sky">
          <div class="play-badge"><svg width="22" height="26" viewBox="0 0 22 26"><path d="M1 1 L21 13 L1 25 Z" fill="#fff"/></svg></div>
        </div>
        <p class="video-caption">Member Video<br>Lorem ipsum<br>sit amet.....</p>
      </div>
      <div class="video-item">
        <div class="video-thumb thumb-dusk" role="img" aria-label="Silhouette of a person against a violet dusk sky">
          <div class="play-badge"><svg width="22" height="26" viewBox="0 0 22 26"><path d="M1 1 L21 13 L1 25 Z" fill="#fff"/></svg></div>
        </div>
        <p class="video-caption">Member Video<br>Lorem ipsum<br>sit amet.....</p>
      </div>
    </aside>

    <a class="buy-button">Buy Now</a>

    <div class="divider"></div>

    <p class="intro">Lorem ipsum dolor sit amet, consectetur adipiscing elit. Nam metus lacus, semper in aliquet et, condimentum auctor nisl. Vestibulum mauris risus, mattis vel mattis non, egestas eu metus. Nulla tempus fermentum mi, non faucibus neque posuere vitae. Ut at elit et nulla blandit pellentesque nec sed mauris. Proin eleifend sollicitudin odio, at viverra ipsum molestie sit amet. Nam dignissim sapien eu libero adipiscing nec molestie purus imperdiet. Duis ullamcorper tincidunt nibh, a tristique ligula cursus lacinia. In dapibus vestibulum quam, sed gravida dolor bibendum non.</p>
  </main>

  <footer class="site-footer">
    <p class="copyright">© Copyright&nbsp; Der Sternenpfad 2012. All Rights Reserved.</p>
    <nav class="social" aria-label="Social links">
      <a class="social-link" aria-label="Social link one"><span></span></a>
      <a class="social-link" aria-label="Social link two"><span></span></a>
      <a class="social-link" aria-label="Social link three"><span></span></a>
      <a class="social-link" aria-label="Social link four"><span></span></a>
    </nav>
  </footer>
</body>
</html>
```